Business Card *

A business card design
Use the logo uploaded in the brief page.
You may use placeholders in your design layouts.
I will provide the actual business card details to the winning designer.

Logo
Place for contact info (name, title, phone, email, etc)

Requirements
Must have
• Logo

```html
<!DOCTYPE html>
<html lang="en">
<head>
<meta charset="utf-8">
<title>Harrowfield Business Card</title>
<link rel="stylesheet" href="https://fonts.googleapis.com/css2?family=Open+Sans:wght@400;600;700&display=swap">
<style>
  :root {
    --stage: #2b2b2b;
    --card-light: #f7f7f7;
    --card-dark: #1c1c1c;
    --brand-green: #2e9e2e;
    --brand-grey: #6b6b6b;
    --text-dark: #2a2a2a;
    --text-muted: #666666;
    --dark-mark: #3a3a3a;
  }
  * { margin: 0; padding: 0; box-sizing: border-box; }
  html, body {
    width: 1200px; height: 997px; overflow: hidden;
    background: var(--stage);
    font-family: "Open Sans", Arial, sans-serif;
  }
  .stage {
    position: relative; width: 1200px; height: 997px;
    display: flex; align-items: center; justify-content: center; gap: 40px;
  }
  .card {
    position: relative; width: 540px; height: 309px;
    box-shadow: 0 10px 30px rgba(0,0,0,.45);
  }
  .card--back { background: var(--card-dark); }
  .card--front { background: var(--card-light); }

  .brand { display: flex; align-items: center; gap: 12px; }
  .brand__dot { width: 22px; height: 22px; border-radius: 50%; }
  .brand__name { font-weight: 700; font-size: 30px; letter-spacing: 1px; text-transform: uppercase; }

  .card--back .brand { position: absolute; left: 50%; top: 50%; transform: translate(-50%, -50%); }
  .card--back .brand__dot { background: var(--dark-mark); width: 30px; height: 30px; }
  .card--back .brand__name { color: var(--dark-mark); font-size: 40px; }

  .card--front .brand { position: absolute; right: 30px; top: 118px; }
  .card--front .brand__dot { background: var(--brand-green); }
  .card--front .brand__name { color: var(--brand-grey); }

  .person { position: absolute; left: 30px; top: 104px; }
  .person__name { color: var(--brand-green); font-weight: 700; font-size: 16px; line-height: 1.2; }
  .person__title { color: var(--text-dark); font-size: 13px; }

  .contact { position: absolute; left: 30px; top: 190px; font-size: 13px; color: var(--text-muted); line-height: 1.35; }
  .contact__address { margin-bottom: 4px; }
  .contact__row { display: flex; align-items: center; gap: 10px; }
  .contact__icon { width: 14px; height: 12px; fill: var(--brand-green); flex: none; }
  .contact__web { color: var(--brand-green); font-weight: 600; font-size: 14px; margin-left: 24px; }
</style>
</head>
<body>
<main class="stage">
  <section class="card card--back" aria-label="Card back">
    <div class="brand">
      <span class="brand__dot"></span>
      <span class="brand__name">Harrowfield</span>
    </div>
  </section>

  <section class="card card--front" aria-label="Card front">
    <div class="person">
      <p class="person__name">Mara Dunley</p>
      <p class="person__title">Pathologist</p>
    </div>

    <div class="contact">
      <p class="contact__address">Unit 8, Canal Road,<br>Pune, India.</p>
      <p class="contact__row">
        <svg class="contact__icon" viewBox="0 0 14 12" aria-hidden="true"><path d="M1 4c0-2 3-3 6-3s6 1 6 3v1h-3V4H4v1H1zM3 6h8l2 5H1z"/></svg>
        <span>0412 780 265</span>
      </p>
      <p class="contact__row">
        <svg class="contact__icon" viewBox="0 0 14 12" aria-hidden="true"><path d="M3 0h8v3H3zM0 4h14v5h-3V7H3v2H0zM4 8h6v4H4z"/></svg>
        <span>003-514-2790</span>
      </p>
      <p class="contact__row">
        <svg class="contact__icon" viewBox="0 0 14 12" aria-hidden="true"><path d="M0 1h14v10H0zM1 2l6 5 6-5v-.2H1z" fill-rule="evenodd"/></svg>
        <span>mara@harrowfield.com</span>
      </p>
      <p class="contact__web">www.harrowfield.com</p>
    </div>

    <div class="brand">
      <span class="brand__dot"></span>
      <span class="brand__name">Harrowfield</span>
    </div>
  </section>
</main>
</body>
</html>
```